Corvena Hotel, city center modern minimal hotel operating all year round, on Rhodes island Greece

city, modern ,all year operating hotel

Target Market(s)

tourists, business agents

Industry/Entity Type

tourism

Coding

Coded - Design and coding required

Number of Pages Required

2 page

Requirements
Must have
• room type photos and descriptions, amenities individual listing (graphic), comments sections, map driving location details
Nice to have
• gallery section, modern and minimal design, amenities section, individual room type descriptions, photos and facilities

```html
<!DOCTYPE html>
<html lang="en">
<head>
<meta charset="utf-8">
<title>Corvena Hotel</title>
<link href="https://fonts.googleapis.com/css2?family=Marcellus&family=Jost:ital,wght@0,400;0,500;0,600;1,400&display=swap" rel="stylesheet">
<style>
:root{
  --green:#1e5a3b;
  --green-dark:#173f2b;
  --band:#22382d;
  --gold:#d1a23b;
  --gold-light:#e2bb5c;
  --ink:#2a2a2a;
  --muted:#6b6b6b;
  --footer:#2b2b2b;
  --white:#ffffff;
}
*{box-sizing:border-box;margin:0;padding:0}
html,body{width:1200px;height:4694px;overflow:hidden}
body{position:relative;background:var(--white);font-family:'Jost',sans-serif;color:var(--ink)}
.serif{font-family:'Marcellus',serif}
section,header,footer{position:absolute;left:0;width:1200px}
.abs{position:absolute}
.btn{position:absolute;background:var(--gold);color:var(--white);font:600 15px 'Jost',sans-serif;letter-spacing:.5px;display:flex;align-items:center;justify-content:center;gap:6px;text-transform:uppercase}
.btn svg{width:13px;height:13px}
.photo{position:absolute}

/* header */
.topbar{top:0;height:40px}
.social-dot{position:absolute;top:12px;width:14px;height:14px;border-radius:50%;background:var(--green)}
.topinfo{position:absolute;top:10px;right:98px;font-size:14px;color:var(--muted);display:flex;gap:20px}
.topinfo span{display:flex;align-items:center;gap:6px}
.brand{position:absolute;display:flex;align-items:center;gap:12px;font-family:'Marcellus',serif;color:var(--green);white-space:nowrap}
.brand i{display:block;background:var(--gold)}
.nav{position:absolute;top:62px;left:544px;display:flex;gap:31px;font-size:16px;color:var(--ink);text-transform:uppercase}

/* hero */
.hero{top:0;height:620px;background:linear-gradient(180deg,#f4f4f3 0%,#eeeeec 60%,#f6f6f5 100%)}
.eyebrow{font-size:17px;letter-spacing:2px;text-transform:uppercase}
.hero-title{position:absolute;left:98px;top:238px;font-family:'Marcellus',serif;font-weight:400;font-size:54px;line-height:66px;color:var(--green);letter-spacing:2px}
.booking{position:absolute;left:98px;top:496px;width:1004px;height:123px;background:var(--green)}
.booking label{position:absolute;top:30px;color:var(--white);font-size:14px;letter-spacing:2px}
.field{position:absolute;top:58px;height:40px;background:var(--white);border:1px solid #d8d8d8;color:#888;font-size:15px;display:flex;align-items:center;justify-content:space-between;padding:0 12px}

/* welcome */
.welcome{top:620px;height:430px}
.frame-top{position:absolute;left:98px;top:25px;width:448px;height:7px;background:var(--green)}
.frame-left{position:absolute;left:98px;top:25px;width:7px;height:352px;background:var(--green)}
.welcome p{position:absolute;left:612px;top:214px;width:490px;font-size:15px;line-height:26px;color:var(--muted)}

/* promotions */
.promotions{top:1050px;height:760px}
.center{text-align:center;width:100%}
.card{position:absolute;overflow:hidden}
.card .name{position:absolute;left:9px;bottom:40px;font-family:'Marcellus',serif;font-size:26px;color:var(--white)}
.card .meta{position:absolute;left:11px;bottom:12px;display:flex;gap:20px;font-size:14px;color:var(--white)}
.card .meta span{display:flex;align-items:center;gap:6px}

/* amenities band */
.amenities{top:1831px;height:237px;background:linear-gradient(90deg,#1f352a,#2a4336 50%,#1f352a)}
.amenity{position:absolute;top:116px;display:flex;gap:12px;align-items:flex-start;color:var(--white)}
.amenity h4{font:400 26px 'Marcellus',serif;line-height:28px}
.amenity small{font-size:14px;letter-spacing:2px;color:#cfd7d2}

/* services */
.services{top:2068px;height:552px}
.services p{position:absolute;left:98px;top:318px;width:405px;font-size:15px;line-height:27px;color:var(--muted)}
.thumb-label{position:absolute;left:969px}
.thumb-label small{display:block;font-size:14px;color:var(--green)}
.thumb-label b{display:block;font:400 22px 'Marcellus',serif;color:var(--gold)}

/* testimonial */
.testimonial{top:2620px;height:536px}
.testi-panel{position:absolute;left:0;top:0;width:612px;height:536px;background:var(--green);border-bottom-right-radius:180px 230px}
.quote{position:absolute;left:103px;top:212px;width:460px;font:italic 400 22px/35px 'Jost',sans-serif;color:var(--white)}
.arrow-btn{position:absolute;top:442px;width:36px;height:36px;border-radius:50%;display:flex;align-items:center;justify-content:center}

/* gallery */
.gallery{top:3156px;height:620px}

/* contact */
.contact{top:3777px;height:541px}
.contact-card{position:absolute;left:700px;top:40px;width:400px;height:474px;background:var(--green);border-radius:60px 0 60px 0}
.contact-title{position:absolute;left:22px;top:40px;font:400 54px/60px 'Marcellus',serif;color:var(--gold);white-space:nowrap}
.input{position:absolute;left:22px;width:356px;height:44px;border:1px solid #9bb5a6;color:var(--white);font-size:15px;padding:10px}

/* footer */
.site-footer{top:4318px;height:376px;background:var(--footer);color:#bdbdbd}
.foot-col{position:absolute;top:72px}
.foot-col h5{font:400 21px 'Marcellus',serif;color:var(--gold);margin-bottom:18px}
.foot-col li{list-style:none;font-size:14px;line-height:36px;color:#c9c9c9}
.foot-col li::before{content:'›';color:var(--gold);margin-right:8px}
.contact-row{display:flex;gap:10px;font-size:14px;line-height:24px;margin-bottom:12px;color:#c9c9c9}
.fsocial{position:absolute;top:222px;width:40px;height:40px;border-radius:50%;background:var(--gold)}
</style>
</head>
<body>

<!-- Hero -->
<header class="hero">
  <div class="topbar">
    <span class="social-dot" style="left:98px"></span>
    <span class="social-dot" style="left:122px"></span>
    <span class="social-dot" style="left:146px"></span>
    <div class="topinfo">
      <span><svg width="14" height="14" viewBox="0 0 24 24"><path fill="#d1a23b" d="M6.6 10.8a15 15 0 006.6 6.6l2.2-2.2c.3-.3.7-.4 1-.2 1.1.4 2.3.6 3.6.6.6 0 1 .4 1 1V20c0 .6-.4 1-1 1A17 17 0 013 4c0-.6.4-1 1-1h3.5c.6 0 1 .4 1 1 0 1.3.2 2.5.6 3.6.1.3 0 .7-.2 1z"/></svg>01 555 0142 77</span>
      <span><svg width="15" height="12" viewBox="0 0 24 18"><rect width="24" height="18" rx="2" fill="#d1a23b"/><path d="M1 2l11 8 11-8" stroke="#fff" stroke-width="2" fill="none"/></svg>info@corvenahotel.com</span>
    </div>
  </div>
  <div class="brand" style="left:98px;top:58px;font-size:36px"><i style="width:30px;height:30px"></i>Corvena Hotel</div>
  <nav class="nav"><span>Home</span><span>About</span><span>Rooms</span><span>News</span><span>Contact</span></nav>
  <div class="btn" style="left:956px;top:51px;width:146px;height:44px">Book Now <svg viewBox="0 0 16 16"><circle cx="8" cy="8" r="8" fill="#fff"/><path d="M6 4l4 4-4 4" stroke="#d1a23b" stroke-width="2" fill="none"/></svg></div>

  <div class="abs eyebrow" style="left:100px;top:212px;color:var(--gold)">Luxury Hotel &amp; Best Resort</div>
  <h1 class="hero-title">ENJOY A LUXURY<br>EXPERIENCE</h1>
  <div class="btn" style="left:100px;top:383px;width:148px;height:42px">Book Now <svg viewBox="0 0 16 16"><circle cx="8" cy="8" r="8" fill="#fff"/><path d="M6 4l4 4-4 4" stroke="#d1a23b" stroke-width="2" fill="none"/></svg></div>

  <form class="booking">
    <label style="left:26px">CHECK-IN</label>
    <label style="left:270px">CHECK-OUT</label>
    <label style="left:510px">GUESTS</label>
    <div class="field" style="left:24px;width:230px">-- / -- / --<svg width="14" height="14" viewBox="0 0 14 14"><rect x="1" y="2" width="12" height="11" fill="none" stroke="#555"/><path d="M1 5h12M4 0v3M10 0v3" stroke="#555"/></svg></div>
    <div class="field" style="left:266px;width:230px">-- / -- / --<svg width="14" height="14" viewBox="0 0 14 14"><rect x="1" y="2" width="12" height="11" fill="none" stroke="#555"/><path d="M1 5h12M4 0v3M10 0v3" stroke="#555"/></svg></div>
    <div class="field" style="left:508px;width:228px">00<svg width="12" height="8" viewBox="0 0 12 8"><path d="M1 1l5 5 5-5" stroke="#555" stroke-width="1.5" fill="none"/></svg></div>
    <div class="btn" style="left:748px;top:58px;width:230px;height:40px;font-size:14px">Check Availability <svg viewBox="0 0 16 16"><circle cx="8" cy="8" r="8" fill="#fff"/><path d="M6 4l4 4-4 4" stroke="#d1a23b" stroke-width="2" fill="none"/></svg></div>
  </form>
</header>

<!-- Welcome -->
<section class="welcome">
  <div class="frame-top"></div>
  <div class="frame-left"></div>
  <div class="photo" role="img" aria-label="Warm-lit hotel lounge with beige sofas and a coffee table" style="left:120px;top:42px;width:445px;height:358px;background:linear-gradient(160deg,#e9dfcf,#b79d7c 55%,#6b5540)"></div>
  <div class="abs eyebrow" style="left:612px;top:106px;color:var(--ink)">Welcome to</div>
  <h2 class="abs serif" style="left:606px;top:128px;font-size:62px;font-weight:400;color:var(--ink);letter-spacing:1px;white-space:nowrap">CORVENA HOTEL</h2>
  <p>Lorem ipsum dolor sit amet, consec adiscing elit. Sed quis faucibus eros. Ut molestie odio est, et ultrices libero tempus eget. Mauris egestas conectetur nisl, sed tempus massa porttitor et. Integer s</p>
  <div class="btn" style="left:612px;top:324px;width:148px;height:40px;font-size:14px">Learn More <svg viewBox="0 0 16 16"><circle cx="8" cy="8" r="8" fill="#fff"/><path d="M6 4l4 4-4 4" stroke="#d1a23b" stroke-width="2" fill="none"/></svg></div>
</section>

<!-- Promotions -->
<section class="promotions">
  <div class="abs center eyebrow" style="top:52px;font-size:18px;color:var(--ink)">Best Monthly</div>
  <h2 class="abs center serif" style="top:72px;font-size:66px;font-weight:400;letter-spacing:2px">PROMOTIONS</h2>

  <div class="card" style="left:98px;top:174px;width:317px;height:246px">
    <div class="photo" role="img" aria-label="Double bed room with orange wall art" style="inset:0;background:linear-gradient(150deg,#e8b44a,#a8784a 45%,#4a3a2e)"></div>
    <div class="name">Double Bed Room</div>
    <div class="meta"><span>&#9786; 2 Guests</span><span>&#9633; 23 FT</span></div>
  </div>
  <div class="card" style="left:441px;top:174px;width:317px;height:519px">
    <div class="photo" role="img" aria-label="Double bed room with wood-panelled wall and wall clock" style="inset:0;background:linear-gradient(180deg,#c9a27a,#9c7a58 55%,#5a4a40)"></div>
    <div class="name">Double Bed Room</div>
    <div class="meta"><span>&#9786; 1 Guests</span><span>&#9633; 18 FT</span></div>
  </div>
  <div class="card" style="left:783px;top:174px;width:317px;height:246px">
    <div class="photo" role="img" aria-label="Family room with grey upholstered bed" style="inset:0;background:linear-gradient(160deg,#e4dbcd,#b5aca2 55%,#6d675f)"></div>
    <div class="name">Family Room</div>
    <div class="meta"><span>&#9786; 4 Guests</span><span>&#9633; 23 FT</span></div>
  </div>
  <div class="card" style="left:98px;top:447px;width:317px;height:246px">
    <div class="photo" role="img" aria-label="Bright single bed room with white linen" style="inset:0;background:linear-gradient(160deg,#efece6,#c8c0b4 55%,#6f6760)"></div>
    <div class="name">Single Bed Room</div>
    <div class="meta"><span>&#9786; 1 Guests</span><span>&#9633; 18 FT</span></div>
  </div>
  <div class="card" style="left:783px;top:447px;width:317px;height:246px">
    <div class="photo" role="img" aria-label="Hotel exterior with balconies and a terrace" style="inset:0;background:linear-gradient(160deg,#d7dde4,#a08b7a 50%,#5e5049)"></div>
    <div class="name">Single Room</div>
    <div class="meta"><span>&#9786; 1 Guests</span><span>&#9633; 18 FT</span></div>
  </div>
</section>

<!-- Amenities -->
<section class="amenities" role="region" aria-label="Amenities">
  <div class="amenity" style="left:98px">
    <svg width="46" height="58" viewBox="0 0 46 58" fill="none" stroke="#d1a23b" stroke-width="2"><circle cx="23" cy="14" r="11"/><circle cx="23" cy="10" r="3"/><path d="M23 25v30M23 40h8M23 48h6"/></svg>
    <div><h4>Smart Key</h4><small>Lorem ipsum dolor</small></div>
  </div>
  <div class="amenity" style="left:362px">
    <svg width="46" height="50" viewBox="0 0 46 50" fill="none" stroke="#d1a23b" stroke-width="2"><path d="M23 4a10 10 0 0110 10c0 8-10 18-10 18S13 22 13 14A10 10 0 0123 4z"/><circle cx="23" cy="14" r="3"/><path d="M3 30l12-4 16 6 12-4v18l-12 4-16-6-12 4z"/></svg>
    <div><h4>GPS</h4><small>Driving Location</small></div>
  </div>
  <div class="amenity" style="left:600px">
    <svg width="46" height="58" viewBox="0 0 46 58" fill="none" stroke="#d1a23b" stroke-width="2"><circle cx="23" cy="14" r="11"/><circle cx="23" cy="10" r="3"/><path d="M23 25v30M23 40h8M23 48h6"/></svg>
    <div><h4>Room Service</h4><small>Lorem ipsum dolor</small></div>
  </div>
  <div class="amenity" style="left:870px">
    <svg width="46" height="50" viewBox="0 0 46 50" fill="none" stroke="#d1a23b" stroke-width="2"><path d="M23 4a10 10 0 0110 10c0 8-10 18-10 18S13 22 13 14A10 10 0 0123 4z"/><circle cx="23" cy="14" r="3"/><path d="M3 30l12-4 16 6 12-4v18l-12 4-16-6-12 4z"/></svg>
    <div><h4>Store Luggage</h4><small>Driving Location</small></div>
  </div>
</section>

<!-- Services -->
<section class="services">
  <div class="abs eyebrow" style="left:98px;top:125px;font-size:18px">Hotel Services</div>
  <h2 class="abs serif" style="left:98px;top:146px;font-size:55px;font-weight:400;line-height:74px;color:var(--ink)">Check all Rooms<br>&amp; Best Suites</h2>
  <p>Lorem ipsum dolor sit amet, consec adiscing elit. Sed quis faucibus eros. Ut molestie odio est, et ultrices libero tempus eget. Mauris egestas conectetur nisl, sed tempus massa porttitor et. Integer semleo felis, nec consequat dui cursus nec.</p>
  <div class="photo" role="img" aria-label="Traveller walking with a red suitcase by the sea" style="left:548px;top:73px;width:365px;height:401px;background:linear-gradient(180deg,#cfe0ea 0%,#7fa3b8 45%,#9c9a90 75%,#8a8680)"></div>
  <div class="photo" role="img" aria-label="Double room thumbnail" style="left:867px;top:140px;width:88px;height:88px;background:linear-gradient(160deg,#ddd5c8,#6f6a64)"></div>
  <div class="photo" role="img" aria-label="Small suite thumbnail" style="left:867px;top:246px;width:88px;height:88px;background:linear-gradient(160deg,#efe6d6,#9a8a74)"></div>
  <div class="photo" role="img" aria-label="Family room thumbnail" style="left:867px;top:352px;width:88px;height:88px;background:linear-gradient(160deg,#c9c4bd,#4e4a46)"></div>
  <div class="thumb-label" style="top:161px"><small>All Excluseive</small><b>Double Room</b></div>
  <div class="thumb-label" style="top:268px"><small>Breakfast</small><b>Small Suite</b></div>
  <div class="thumb-label" style="top:374px"><small>Drinks Included</small><b>Family Room</b></div>
</section>

<!-- Testimonial -->
<section class="testimonial">
  <div class="photo" role="img" aria-label="Folded white towels with a frangipani flower on a bed" style="left:580px;top:0;width:620px;height:536px;background:linear-gradient(160deg,#f4f1ec,#d9d3ca 55%,#8a7c6c)"></div>
  <div class="testi-panel"></div>
  <div class="abs" style="left:98px;top:94px;font-size:19px;letter-spacing:1.5px;color:var(--white)">Testimonial</div>
  <h2 class="abs serif" style="left:103px;top:112px;font-size:56px;font-weight:400;color:var(--gold)">What Client Say</h2>
  <div class="abs serif" style="left:92px;top:196px;font-size:60px;color:#3f7a58">&ldquo;</div>
  <p class="quote">Nullam a turpis eu est posuere aliquet nec nec nisl. Nam ac lectus semr, eleifend felis ultrices, condimentum metus. Donec ut dui dictum, luctus justo in, luctus libero.</p>
  <div class="abs" style="left:98px;top:372px;font-size:22px;letter-spacing:2px;color:var(--gold)">&#9733;&#9733;&#9733;&#9733;&#9733;</div>
  <div class="abs" style="left:98px;top:408px;font-size:28px;font-weight:500;color:var(--white)">Elena Marris</div>
  <div class="arrow-btn" style="left:432px;background:#9a9a9a"><svg width="14" height="14" viewBox="0 0 14 14"><path d="M9 2L4 7l5 5" stroke="#fff" stroke-width="2.5" fill="none"/></svg></div>
  <div class="arrow-btn" style="left:478px;background:var(--white)"><svg width="14" height="14" viewBox="0 0 14 14"><path d="M5 2l5 5-5 5" stroke="#1e5a3b" stroke-width="2.5" fill="none"/></svg></div>
</section>

<!-- Gallery -->
<section class="gallery">
  <h2 class="abs center serif" style="top:72px;font-size:58px;font-weight:400">Gallery</h2>
  <div class="photo" role="img" aria-label="Dark modern bedroom with upholstered headboard" style="left:98px;top:160px;width:252px;height:359px;background:linear-gradient(170deg,#3a3530,#8a7460 50%,#2a2622)"></div>
  <div class="photo" role="img" aria-label="Dining corner with table and chairs" style="left:350px;top:160px;width:250px;height:179px;background:linear-gradient(160deg,#e8e2d8,#7d6d5e)"></div>
  <div class="photo" role="img" aria-label="Bright bedroom with large windows" style="left:350px;top:339px;width:250px;height:180px;background:linear-gradient(160deg,#e1e8ef,#aab6c2 60%,#6c7480)"></div>
  <div class="photo" role="img" aria-label="Guest walking along a hotel corridor with luggage" style="left:600px;top:160px;width:249px;height:359px;background:linear-gradient(180deg,#d8b98a,#8c6a46 55%,#3e2f22)"></div>
  <div class="photo" role="img" aria-label="Housekeeper making a bed" style="left:849px;top:160px;width:251px;height:179px;background:linear-gradient(160deg,#ece9e4,#b4aba0)"></div>
  <div class="photo" role="img" aria-label="Guest relaxing at the edge of a pool" style="left:849px;top:339px;width:251px;height:180px;background:linear-gradient(180deg,#cfe3e6,#6fb3c0 60%,#3c8694)"></div>
</section>

<!-- Contact -->
<section class="contact">
  <div class="photo" role="img" aria-label="Breakfast tray with juice and pastries on a bed" style="inset:0;background:linear-gradient(110deg,#e8e4dc,#c9b9a2 40%,#8a5a3a 60%,#e5e1da)"></div>
  <form class="contact-card">
    <h2 class="contact-title">Get In Touch</h2>
    <div class="input" style="top:131px">Name</div>
    <div class="input" style="top:184px">Email</div>
    <div class="input" style="top:237px">Phone</div>
    <div class="input" style="top:290px;height:84px">Your Message</div>
    <div class="btn" style="left:22px;top:388px;width:145px;height:40px;font-size:14px">Submit Now <svg viewBox="0 0 16 16"><circle cx="8" cy="8" r="8" fill="#fff"/><path d="M6 4l4 4-4 4" stroke="#d1a23b" stroke-width="2" fill="none"/></svg></div>
  </form>
</section>

<!-- Footer -->
<footer class="site-footer">
  <div class="brand" style="left:98px;top:100px;font-size:40px;color:var(--green)"><i style="width:32px;height:32px"></i>Corvena Hotel</div>
  <span class="fsocial" style="left:103px"></span>
  <span class="fsocial" style="left:160px"></span>
  <span class="fsocial" style="left:217px"></span>

  <div class="foot-col" style="left:419px">
    <h5>Quick Links</h5>
    <ul><li>Home</li><li>About</li><li>Rooms</li><li>News</li><li>Contact</li></ul>
  </div>
  <div class="foot-col" style="left:589px;width:220px">
    <h5>Contact Info</h5>
    <div class="contact-row"><svg width="14" height="18" viewBox="0 0 14 18"><path d="M7 0a7 7 0 017 7c0 5-7 11-7 11S0 12 0 7a7 7 0 017-7z" fill="#d1a23b"/><circle cx="7" cy="7" r="2.5" fill="#2b2b2b"/></svg><span>24 Harbor Lane,<br>Rhodes island Greece</span></div>
    <div class="contact-row"><svg width="14" height="14" viewBox="0 0 24 24"><path fill="#d1a23b" d="M6.6 10.8a15 15 0 006.6 6.6l2.2-2.2c.3-.3.7-.4 1-.2 1.1.4 2.3.6 3.6.6.6 0 1 .4 1 1V20c0 .6-.4 1-1 1A17 17 0 013 4c0-.6.4-1 1-1h3.5c.6 0 1 .4 1 1 0 1.3.2 2.5.6 3.6.1.3 0 .7-.2 1z"/></svg><span>01 555 0142 77</span></div>
    <div class="contact-row"><svg width="15" height="12" viewBox="0 0 24 18"><rect width="24" height="18" rx="2" fill="#d1a23b"/><path d="M1 2l11 8 11-8" stroke="#2b2b2b" stroke-width="2" fill="none"/></svg><span>info@corvenahotel.com</span></div>
  </div>
  <div class="foot-col" style="left:831px;width:270px">
    <h5>Newsletter</h5>
    <p style="font-size:14px;line-height:24px;color:#c9c9c9">Sed quis faucibus eros. Ut molestie odio est, et ultrices libero tempus eget.</p>
    <div style="margin-top:32px;border-bottom:1px solid #d1a23b;padding-bottom:10px;font-size:14px;color:#c9c9c9;display:flex;justify-content:space-between">Enter email address<svg width="16" height="16" viewBox="0 0 16 16"><path d="M1 8L15 1 11 15 8 9z" fill="#d1a23b"/></svg></div>
  </div>

  <div class="abs" style="left:98px;top:310px;width:1004px;height:1px;background:#444"></div>
  <div class="abs center" style="top:337px;font-size:14px;color:#a8a8a8">© 2022 <span style="color:var(--gold)">Corvena Hotel</span>. All right reserved</div>
</footer>

</body>
</html>
```